Sales Brochure- Generic Line Card 215mm x 140mm

Design a double-sided brochure similar to the attached sample. Cover Page contains a logo and theme that never changes. However, the background picture and the description text on the lower corner will be changed to advertise multiple services. Reverse-side contains Detailed Descriptive text related to the picture on Cover Page as well as Logo and Contact information for the business. Use the Ridgeline Controls website www.ridgelinecontrols.ca for theme, color and contact information. Also, use attached business card design for theme to match. Use the supplied logo. SIZE 215mm x 140mm

Font styles to use
Sans Serif

Colors

Designer to choose colors to be used in the design.

Requirements
Must have
• Look Similar to Sample Brochure but include Ridgeline Controls theme and colors

```html
<!DOCTYPE html>
<html lang="en">
<head>
<meta charset="utf-8">
<title>Ridgeline Controls – Machining Line Card</title>
<link rel="stylesheet" href="https://fonts.googleapis.com/css2?family=Montserrat:wght@300;400;500;600;700;800&display=swap">
<style>
  :root{
    --stage:#8a8a8a;
    --teal:#1f9a98;
    --teal-deep:#0f5553;
    --teal-dark:#0a2f2f;
    --orange:#ef6a23;
    --ink:#121416;
    --white:#ffffff;
    --grey-text:#cfd3d4;
  }
  *{box-sizing:border-box;margin:0;padding:0}
  html,body{width:1200px;height:2400px;overflow:hidden}
  body{background:var(--stage);font-family:"Montserrat",Arial,sans-serif;position:relative}
  .card{position:absolute;left:60px;width:1080px;height:642px;overflow:hidden;box-shadow:0 10px 24px rgba(0,0,0,.35)}
  .card--front{top:527px}
  .card--back{top:1231px;background:var(--ink)}

  /* front */
  .front__photo{position:absolute;inset:0;background:
    radial-gradient(circle at 72% 35%, #3fb2ae 0%, #1d8583 30%, #0f4f4e 62%, #082726 100%)}
  .front__rings{position:absolute;inset:0}
  .front__badge{position:absolute;left:48px;top:324px;width:298px;height:298px;border-radius:50%;background:var(--white);display:flex;align-items:center;justify-content:center}
  .front__badge-label{width:100%;text-align:center;color:var(--teal-deep);font-weight:700;font-size:34px;letter-spacing:1px;padding:16px 0;border-top:4px solid var(--teal-deep);border-bottom:4px solid var(--teal-deep)}
  .brand{position:absolute;left:677px;top:52px;width:403px;height:74px;background:var(--white);display:flex;align-items:center;padding-left:26px}
  .brand__mark{width:22px;height:22px;background:var(--teal-deep);margin-right:12px;flex:none}
  .brand__name{font-weight:800;font-size:25px;color:var(--teal-deep);letter-spacing:.3px;text-transform:uppercase;white-space:nowrap}
  .brand__bar{position:absolute;right:0;top:0;width:34px;height:100%;background:var(--orange)}
  .tagline{position:absolute;left:700px;top:404px;padding-left:22px;border-left:3px solid var(--white);color:var(--white);font-size:37px;line-height:1.28;font-weight:300;letter-spacing:1px}
  .tagline strong{font-weight:700}

  /* back */
  .back__title{position:absolute;left:70px;top:42px;padding-left:16px;border-left:3px solid var(--orange);color:var(--orange);font-weight:300;font-size:37px;line-height:1.18;letter-spacing:.5px}
  .back__intro{position:absolute;left:504px;top:42px;width:550px;color:var(--grey-text);font-size:15.5px;line-height:1.5}
  .back__contact{position:absolute;left:504px;top:186px;display:flex;align-items:center;gap:10px;font-size:15px;white-space:nowrap}
  .back__contact-mark{width:14px;height:14px;background:var(--teal);flex:none}
  .back__contact-name{color:var(--white);font-weight:700;text-transform:uppercase;letter-spacing:.5px}
  .back__contact-web{color:var(--orange);font-weight:500;padding-left:10px;border-left:2px solid var(--orange)}
  .capabilities{position:absolute;top:240px;list-style:none}
  .capabilities--left{left:60px}
  .capabilities--right{left:653px}
  .capabilities li{display:flex;align-items:center;height:41px;color:var(--grey-text);font-size:17px}
  .capabilities svg{width:20px;height:20px;margin-right:18px;flex:none}
  .back__band{position:absolute;left:0;bottom:0;width:100%;height:140px;background:linear-gradient(90deg,var(--teal) 0%,var(--teal) 60%,#16807e 100%)}
  .services{position:absolute;left:50px;top:18px;list-style:none}
  .services li{display:flex;align-items:center;height:34px;color:var(--white);font-weight:700;font-size:17px;letter-spacing:.3px;white-space:nowrap}
  .services svg{width:22px;height:22px;margin-right:18px;flex:none}
  .gallery{position:absolute;left:480px;top:24px;display:flex;gap:12px}
  .gallery__item{position:relative;width:137px;height:103px}
  .gallery__photo{position:absolute;inset:0;background:linear-gradient(135deg,#5d6466,#2c3234 70%,#1a1d1e)}
  .gallery__label{position:absolute;left:0;bottom:0;width:100%;background:var(--orange);color:var(--white);font-weight:700;font-size:12px;text-align:center;padding:4px 0;white-space:nowrap}
</style>
</head>
<body>

<section class="card card--front">
  <div class="front__photo" role="img" aria-label="Teal-toned photograph of a CNC lathe turret and spindle"></div>
  <svg class="front__rings" viewBox="0 0 1080 642" fill="none" stroke="#ffffff" stroke-width="3" stroke-dasharray="12 10">
    <circle cx="197" cy="473" r="205"/>
    <circle cx="520" cy="300" r="440"/>
  </svg>
  <div class="brand">
    <span class="brand__mark"></span>
    <span class="brand__name">Ridgeline Controls</span>
    <span class="brand__bar"></span>
  </div>
  <div class="front__badge"><div class="front__badge-label">MACHINING</div></div>
  <div class="tagline">PIONEERING<br><strong>RESPONSIVE</strong><br>MACHINING</div>
</section>

<section class="card card--back">
  <h2 class="back__title">COMPUTER<br>NUMERIC<br>CONTROL (CNC)</h2>
  <p class="back__intro">CNC machining offers the most efficient method of producing steel and plastic components. The CNC is programmed using computer code to generate a digital machining process that can be repeated and precisely controlled. Repetitive tasks such as drilling, threading, and tapping are made simple using this technology.</p>
  <div class="back__contact">
    <span class="back__contact-mark"></span>
    <span class="back__contact-name">Ridgeline Controls</span>
    <span class="back__contact-web">www.ridgelinecontrols.ca</span>
  </div>

  <ul class="capabilities capabilities--left">
    <li><svg viewBox="0 0 20 20"><circle cx="10" cy="10" r="10" fill="#1f9a98"/><path d="M5.5 10.2l3 3 6-6" stroke="#121416" stroke-width="2.4" fill="none"/></svg>Lathe &amp; Turning Centers up to 36" Dia.</li>
    <li><svg viewBox="0 0 20 20"><circle cx="10" cy="10" r="10" fill="#1f9a98"/><path d="M5.5 10.2l3 3 6-6" stroke="#121416" stroke-width="2.4" fill="none"/></svg>Mill &amp; Machining Centers up to 120" L</li>
    <li><svg viewBox="0 0 20 20"><circle cx="10" cy="10" r="10" fill="#1f9a98"/><path d="M5.5 10.2l3 3 6-6" stroke="#121416" stroke-width="2.4" fill="none"/></svg>Complex Multi-Axis Machining up to 8-Axis</li>
    <li><svg viewBox="0 0 20 20"><circle cx="10" cy="10" r="10" fill="#1f9a98"/><path d="M5.5 10.2l3 3 6-6" stroke="#121416" stroke-width="2.4" fill="none"/></svg>Swiss Screw Machining</li>
    <li><svg viewBox="0 0 20 20"><circle cx="10" cy="10" r="10" fill="#1f9a98"/><path d="M5.5 10.2l3 3 6-6" stroke="#121416" stroke-width="2.4" fill="none"/></svg>Deep Hole Drilling/Trepanning</li>
    <li><svg viewBox="0 0 20 20"><circle cx="10" cy="10" r="10" fill="#1f9a98"/><path d="M5.5 10.2l3 3 6-6" stroke="#121416" stroke-width="2.4" fill="none"/></svg>CNC Honing &amp; Grinding</li>
  </ul>
  <ul class="capabilities capabilities--right">
    <li><svg viewBox="0 0 20 20"><circle cx="10" cy="10" r="10" fill="#1f9a98"/><path d="M5.5 10.2l3 3 6-6" stroke="#121416" stroke-width="2.4" fill="none"/></svg>CNC Laser &amp; Cladding</li>
    <li><svg viewBox="0 0 20 20"><circle cx="10" cy="10" r="10" fill="#1f9a98"/><path d="M5.5 10.2l3 3 6-6" stroke="#121416" stroke-width="2.4" fill="none"/></svg>CNC Press</li>
    <li><svg viewBox="0 0 20 20"><circle cx="10" cy="10" r="10" fill="#1f9a98"/><path d="M5.5 10.2l3 3 6-6" stroke="#121416" stroke-width="2.4" fill="none"/></svg>CNC Plasma &amp; Water Jet</li>
    <li><svg viewBox="0 0 20 20"><circle cx="10" cy="10" r="10" fill="#1f9a98"/><path d="M5.5 10.2l3 3 6-6" stroke="#121416" stroke-width="2.4" fill="none"/></svg>Oil Field and Custom Threading</li>
    <li><svg viewBox="0 0 20 20"><circle cx="10" cy="10" r="10" fill="#1f9a98"/><path d="M5.5 10.2l3 3 6-6" stroke="#121416" stroke-width="2.4" fill="none"/></svg>3D Surfacing and Mold Machining</li>
    <li><svg viewBox="0 0 20 20"><circle cx="10" cy="10" r="10" fill="#1f9a98"/><path d="M5.5 10.2l3 3 6-6" stroke="#121416" stroke-width="2.4" fill="none"/></svg>Large Capacity Band Saw Cutting</li>
  </ul>

  <div class="back__band">
    <ul class="services">
      <li><svg viewBox="0 0 22 22" fill="#ffffff"><rect x="2" y="4" width="18" height="5"/><rect x="9" y="9" width="4" height="11"/></svg>SWISS SCREW &amp; SMALL PARTS</li>
      <li><svg viewBox="0 0 22 22" fill="none" stroke="#ffffff" stroke-width="2.4"><circle cx="11" cy="11" r="4"/><path d="M11 1v4M11 17v4M1 11h4M17 11h4M4 4l3 3M15 15l3 3M4 18l3-3M15 7l3-3"/></svg>AUTOMATION</li>
      <li><svg viewBox="0 0 22 22" fill="none" stroke="#ffffff" stroke-width="2.4"><circle cx="11" cy="12" r="8"/><path d="M11 7v5l3 2M3 3l3 2M19 3l-3 2"/></svg>24HR SERVICE, REPAIR AND WELDING</li>
    </ul>
    <div class="gallery">
      <figure class="gallery__item"><div class="gallery__photo" role="img" aria-label="Photo of a lathe turning a part"></div><figcaption class="gallery__label">LATHE / TURNING</figcaption></figure>
      <figure class="gallery__item"><div class="gallery__photo" role="img" aria-label="Photo of a milling machine cutting metal"></div><figcaption class="gallery__label">MILLING</figcaption></figure>
      <figure class="gallery__item"><div class="gallery__photo" role="img" aria-label="Photo of a Swiss screw machine"></div><figcaption class="gallery__label">SWISS</figcaption></figure>
      <figure class="gallery__item"><div class="gallery__photo" role="img" aria-label="Photo of a 5-axis machining center"></div><figcaption class="gallery__label">5-AXIS</figcaption></figure>
    </div>
  </div>
</section>

</body>
</html>
```